Website: Orvalink Business Consultants, Qianhai SEZ, China

Our client is a business consultancy firm and will be the first to set up in the Qianhai Shenzhen-Hong Kong Modern Service Industry Cooperation Zone, China So we need a corporate website concept that engages service, finance and technology sector companies. The company can provide all the necessary services needed to set up shop in Qianhai. They are looking for a modern, international, reliable and strong image.

Here are some websites for reference prupose:

http://www.brenwickpartners.example/ (we like the dynamic banner and clear, clean layout of this website)

http://www.dovetrassadvisory.example/ (we like the background city image, use of light font, hover over menu functions and color scheme - purple and grey)

http://www.pelmo.example/ (we like the simplicity of this website, clear lines and we like the dynamic banner)
Updates

Hello, We are currently undecided between three logo designs.  All three have been uploaded to the design brief so that you can use them as reference for the website design. Thx

Also please take note of the addition menu selection 'About Qianhai'. Thx

Hello all Designers, First of all we want thank you for participating in our website competition, the calibre of design was high and we appreciated the expedience. Our company is Quillon Reach Web Design and Internet Marketing based in Shenzhen, China. We anticipate rapid growth in the Chinese domestic market as the country shifts in to a service sector economy. We hope to continue building reliable working relationships with you based on idea sharing and constructive feedback. Once again, Thankyou, QR Team

Target Market(s)

International finance and technology companies looking to set up in Qianhai Special Economic Zone, China

Industry/Entity Type

Finance

Requirements
Must have
• Initial design for home page and in later selection stages a secondary page will be required.

The design should be for PSD concepts only no code!

Menu bar, Photo banner -
A. Photo banner and text overlay,
B.Photo Banner and text description to left or right.

Social Connect icons, Site search bar (top right), Logo space (top left).

Menu bar at top with Home, About Us, About Qianhai, Services, Portfolio, Partners, Our Team Contact Us.

Standard 3-4 box layout - Banner at top and 2-3 boxes under banner.

Colour scheme- A. Purple and Blue, must have light background/body
B. Shades of white, black and grey.

Simple, clear, clean, sharp.

```html
<!DOCTYPE html>
<html lang="en">
<head>
<meta charset="utf-8">
<title>Orvalink Business Consultants</title>
<link href="https://fonts.googleapis.com/css2?family=Arimo:wght@400;700&family=Poiret+One&family=Raleway:wght@400;500&display=swap" rel="stylesheet">
<style>
:root{
  --white:#ffffff;
  --line:#cfcfcf;
  --text:#333333;
  --purple:#5b2a5e;
  --purple-deep:#4a1240;
  --magenta:#b0479a;
  --teal:#3d7a92;
  --nav-active:#78b4e4;
  --card-band:#1d5e9a;
  --btn:#cfe4f6;
  --banner-a:#cdd6e0;
  --banner-b:#9eaab8;
  --banner-panel:rgba(200,185,210,.55);
}
*{box-sizing:border-box;margin:0;padding:0}
html,body{width:1120px;height:1200px;overflow:hidden;background:var(--white)}
body{font-family:"Arimo",Arial,sans-serif;color:var(--text);position:relative}
.abs{position:absolute}
.rule{position:absolute;left:0;width:1120px;height:1px;background:var(--line)}

.social{top:6px;right:110px;display:flex;gap:6px}
.social span{font-size:10px;color:var(--purple);display:flex;align-items:center;gap:3px}
.social span::before{content:"";width:8px;height:8px;background:var(--purple);display:block}

.brand{left:104px;top:78px;display:flex;align-items:center;gap:10px}
.brand-mark{width:62px;height:62px;border-radius:50%;background:var(--magenta)}
.brand-name{font-family:"Raleway",sans-serif;font-size:24px;color:var(--magenta);letter-spacing:1px;line-height:1}
.brand-name small{display:block;font-size:9px;letter-spacing:4px;color:var(--purple);margin-top:4px}

.search{left:857px;top:67px;width:174px;height:23px;border:1px solid #d8c6dc;background:#fdf2fb;display:flex;align-items:center}
.search span{flex:1;padding-left:25px;font-size:14px;color:#a79aa8}
.search svg{width:42px;height:21px;border-left:1px solid #d8c6dc}

.nav{left:355px;top:118px;width:671px;height:56px;border:1px solid #ddd;background:#fafafa;display:flex;align-items:center;padding-left:6px}
.nav a{font-size:13px;color:#222;text-decoration:none;padding:10px 6px}
.nav a.active{background:var(--nav-active);color:#222}
.nav i{color:#bbb;font-style:normal;padding:0 3px}
.pointer{left:547px;top:172px;width:0;height:0;border-left:6px solid transparent;border-right:6px solid transparent;border-top:6px solid var(--nav-active)}
.dropdown{left:482px;top:176px;width:136px;background:#fff;border:1px solid #e0e0e0;box-shadow:0 2px 4px rgba(0,0,0,.15);padding:2px 6px}
.dropdown a{display:block;font-size:11.5px;color:var(--purple);text-decoration:none;text-align:center;padding:6px 0;border-bottom:1px solid #e6e6e6}
.dropdown a:last-child{border-bottom:0}

.banner{left:100px;top:208px;width:930px;height:402px;border:1px solid #ddd;padding:3px}
.banner-photo{width:100%;height:100%;background:linear-gradient(180deg,var(--banner-a),var(--banner-b))}
.banner-panel{left:104px;top:212px;width:301px;height:394px;background:var(--banner-panel);padding:30px 32px;color:#fff}
.arrows{font-size:18px;letter-spacing:10px;color:#fff}
.banner-panel h1{font-size:23px;line-height:24px;margin-top:36px;font-weight:700}
.banner-panel p.lead{font-size:14px;line-height:16px;margin-top:25px;color:#f1eef5}
.banner-panel p.note{font-size:10px;line-height:12px;margin-top:70px;color:#f1eef5}
.banner-grid{position:absolute;pointer-events:none}

.tagline{left:0;width:1120px;top:618px;text-align:center}
.tagline h2{font-family:"Poiret One",sans-serif;font-weight:400;font-size:30px;color:var(--teal);letter-spacing:1px}
.tagline p{font-size:15px;color:var(--purple);letter-spacing:.5px;margin-top:4px}

.section-title{font-family:"Poiret One",sans-serif;font-size:20px;color:var(--purple);display:flex;align-items:center;gap:7px}
.section-title::before{content:"";border-top:5px solid transparent;border-bottom:5px solid transparent;border-left:6px solid var(--card-band)}

.card{top:743px;width:222px;height:242px}
.card-photo{height:181px;border:1px solid #ddd;padding:3px;background:#fff}
.card-photo div{width:100%;height:100%}
.card-band{height:58px;background:var(--card-band);color:#fff;font-size:11.5px;line-height:12px;padding:5px 22px;text-align:justify}
.card-band b{display:inline-block;margin-top:7px;background:var(--btn);color:#1a3a5a;font-weight:400;font-size:11px;padding:2px 6px;border:1px solid #fff;box-shadow:0 0 0 1px #2b4f75}

.client{top:1044px;width:108px;height:58px;border:1px solid #ccc;box-shadow:0 1px 2px rgba(0,0,0,.15);display:flex;align-items:center;justify-content:center;gap:5px;font-size:13px;font-weight:700;color:#2a2a2a}
.client::before{content:"";width:8px;height:8px;border-radius:50%;background:#2a2a2a}
.vline{width:1px;height:58px;background:var(--line);top:1044px}

.footer{left:0;top:1128px;width:1120px;height:72px;background:radial-gradient(ellipse at 40% 50%,#7a2c6f 0%,var(--purple-deep) 70%);color:#fff}
.footer nav{display:flex;justify-content:center;padding-top:15px;font-size:12px}
.footer nav a{color:#fff;text-decoration:none;padding:0 20px;border-right:1px solid #b68bb0}
.footer nav a:last-child{border-right:0}
.footer p{text-align:center;font-size:11.5px;margin-top:18px;letter-spacing:.3px}
</style>
</head>
<body>
<div class="social abs">
  <span>Friendra</span><span>Chirpa</span><span>Globix</span><span>Pixloo</span><span>Pinora</span>
</div>
<div class="rule" style="top:37px"></div>

<div class="brand abs">
  <div class="brand-mark"></div>
  <div class="brand-name">ORVALINK<small>BUSINESS CONSULTING</small></div>
</div>

<div class="search abs">
  <span>search</span>
  <svg viewBox="0 0 42 21"><circle cx="19" cy="9" r="4" fill="none" stroke="#a79aa8" stroke-width="2"/><line x1="22" y1="12" x2="27" y2="16" stroke="#a79aa8" stroke-width="2.5"/></svg>
</div>

<nav class="nav abs">
  <a href="#">Home</a><i>/</i><a href="#">About Us</a><i>/</i><a class="active" href="#">About Qianhai</a><i>/</i><a href="#">Services</a><i>/</i><a href="#">Portfolio</a><i>/</i><a href="#">Partners</a><i>/</i><a href="#">Our Team</a><i>/</i><a href="#">contact Us</a>
</nav>
<div class="pointer abs"></div>
<div class="dropdown abs">
  <a href="#">Lorem Ipsum</a><a href="#">Lorem Ipsum</a><a href="#">Lorem Ipsum</a><a href="#">Lorem Ipsum</a>
</div>

<div class="banner abs">
  <div class="banner-photo" role="img" aria-label="Night view of a dense city skyline by the harbour"></div>
</div>
<div class="banner-panel abs">
  <div class="arrows">‹ ›</div>
  <h1>Nemo enim ipsam voluptatem quia voluptas sit</h1>
  <p class="lead">sed quia consequuntur magni eos qui ratione voluptatem sequi nesciunt.</p>
  <p class="note">eaque ipsa quae ab illo inventore veritatis et quasi architecto beatae vitae dicta sunt explicabo.</p>
</div>

<div class="tagline abs">
  <h2>Sed ut perspiciatis unde omnis iste natus error sit</h2>
  <p>laudantium, totam rem aperiam</p>
</div>
<div class="rule" style="top:697px"></div>

<div class="section-title abs" style="left:106px;top:708px">Lorem Ipsum</div>

<div class="card abs" style="left:102px">
  <div class="card-photo"><div role="img" aria-label="Close-up of a hand adjusting a wristwatch" style="background:linear-gradient(135deg,#efe4e0,#c9aa98)"></div></div>
  <div class="card-band">Lorem ipsum dolor sit amet, consectetur adipisicing elit...<br><b>Read More</b></div>
</div>
<div class="card abs" style="left:337px">
  <div class="card-photo"><div role="img" aria-label="Businesswoman with a team of colleagues in an office" style="background:linear-gradient(135deg,#b9c8d8,#3a4454)"></div></div>
  <div class="card-band">Lorem ipsum dolor sit amet, consectetur adipisicing elit...<br><b>Read More</b></div>
</div>
<div class="card abs" style="left:571px">
  <div class="card-photo"><div role="img" aria-label="Businessman standing in front of city towers" style="background:linear-gradient(180deg,#c9d4e0,#5a6470)"></div></div>
  <div class="card-band">Lorem ipsum dolor sit amet, consectetur adipisicing elit...<br><b>Read More</b></div>
</div>
<div class="card abs" style="left:806px">
  <div class="card-photo"><div role="img" aria-label="Hand typing on a laptop keyboard" style="background:linear-gradient(135deg,#f2f2f2,#555)"></div></div>
  <div class="card-band">Lorem ipsum dolor sit amet, consectetur adipisicing elit...<br><b>Read More</b></div>
</div>

<div class="rule" style="top:1016px"></div>

<div class="section-title abs" style="left:106px;top:1062px">Our Clients</div>
<div class="vline abs" style="left:311px"></div>
<div class="client abs" style="left:342px">Norvane</div>
<div class="client abs" style="left:478px">Brixola</div>
<div class="client abs" style="left:614px">Kestrel</div>
<div class="client abs" style="left:750px">Datamere</div>
<div class="vline abs" style="left:887px"></div>

<footer class="footer abs">
  <nav><a href="#">Home</a><a href="#">About Us</a><a href="#">About Qianhai</a><a href="#">Services</a><a href="#">Portfolio</a><a href="#">Partners</a><a href="#">Our Team</a><a href="#">Contact Us</a></nav>
  <p>copyright © 2013 Orvalink. All Rights Reserved</p>
</footer>
</body>
</html>
```